Business Card Design Project

I need a business card designed from scratch. I have an existing logo that I can upload in Illustrator for modification or redesign.

The Company is called Rank Harbor http://rankharbor.com.au and we provide Search Engine Optimization services to Australian businesses. The current logo signifies an increase in visitors, profits etc...

There are no restrictions as to the redesign - colours, style etc are all open to change.

Cards will be full colour and one sided printed at http://www.printlorvex.com.au so check their requirements for file format and sizes etc.

I will expect all original files upon completion of project.

Target Market(s)

Any business with a web site looking to improve their search engine rankings

Industry/Entity Type

Business

Requirements
Must have
• I like modern, sleek designs. Clean, not fussy, uncluttered.

```html
<!DOCTYPE html>
<html lang="en">
<head>
<meta charset="utf-8">
<title>Rank Harbor – Business Card</title>
<link href="https://fonts.googleapis.com/css2?family=Nunito+Sans:wght@400;600;800&display=swap" rel="stylesheet">
<style>
  :root {
    --page: #f4f4f6;
    --card: #e9e9f0;
    --blue: #2f6ca8;
    --blue-deep: #245a92;
    --blue-light: #4a86c0;
    --yellow: #f2c230;
    --ink: #1c1c24;
    --ink-soft: #3a3a46;
  }
  * { box-sizing: border-box; margin: 0; padding: 0; }
  html, body { width: 1200px; height: 952px; overflow: hidden; background: var(--page); }
  body { font-family: "Nunito Sans", Arial, sans-serif; color: var(--ink); }

  .business-card {
    position: absolute;
    left: 354px; top: 46px;
    width: 491px; height: 860px;
    background: linear-gradient(165deg, #f1f1f7 0%, var(--card) 60%, #e3e3ed 100%);
    overflow: hidden;
    box-shadow: 0 10px 30px rgba(30, 40, 70, .15);
  }

  .brand-lockup {
    position: absolute; left: 0; right: 0; top: 130px;
    display: flex; align-items: center; justify-content: center; gap: 14px;
  }
  .brand-dot { width: 22px; height: 22px; border-radius: 50%; background: var(--yellow); flex: none; }
  .brand-name {
    font-weight: 800; font-size: 46px; color: var(--blue);
    letter-spacing: -.5px; line-height: 1;
  }

  .edge-tab { position: absolute; left: 0; width: 24px; }
  .edge-tab--yellow { top: 318px; height: 60px; background: var(--yellow); }
  .edge-tab--blue { top: 378px; height: 95px; background: var(--blue); }

  .contact-block { position: absolute; left: 56px; top: 312px; }
  .person-name {
    font-weight: 800; font-size: 30px; letter-spacing: .5px;
    text-transform: uppercase; line-height: 1;
  }
  .person-role { font-size: 15px; color: var(--ink-soft); margin-top: 5px; }
  .contact-list { list-style: none; margin-top: 16px; }
  .contact-item {
    display: flex; align-items: center; gap: 12px;
    font-size: 17px; line-height: 1.6; color: var(--ink);
  }
  .contact-icon { width: 17px; height: 17px; flex: none; }

  .ribbon-band {
    position: absolute; left: 0; right: 0; bottom: 0; height: 355px;
    background: linear-gradient(180deg, var(--blue-light) 0%, var(--blue) 45%, var(--blue-deep) 100%);
  }
</style>
</head>
<body>
  <main class="business-card">
    <div class="brand-lockup">
      <span class="brand-dot"></span>
      <span class="brand-name">Rank Harbor</span>
    </div>

    <div class="edge-tab edge-tab--yellow"></div>
    <div class="edge-tab edge-tab--blue"></div>

    <section class="contact-block">
      <h1 class="person-name">Dale Mercer</h1>
      <p class="person-role">Internet Marketing Consultant</p>
      <ul class="contact-list">
        <li class="contact-item">
          <svg class="contact-icon" viewBox="0 0 24 24" aria-hidden="true"><path fill="var(--blue)" d="M6.6 10.8a15.1 15.1 0 0 0 6.6 6.6l2.2-2.2c.3-.3.7-.4 1-.2 1.1.4 2.3.6 3.6.6.6 0 1 .4 1 1V20c0 .6-.4 1-1 1A17 17 0 0 1 3 4c0-.6.4-1 1-1h3.5c.6 0 1 .4 1 1 0 1.3.2 2.5.6 3.6.1.3 0 .7-.2 1z"/></svg>
          1300 482915
        </li>
        <li class="contact-item">
          <svg class="contact-icon" viewBox="0 0 24 24" aria-hidden="true"><rect x="2.5" y="5" width="19" height="14" fill="none" stroke="var(--blue)" stroke-width="1.8"/><path d="M2.5 5l9.5 8 9.5-8" fill="none" stroke="var(--blue)" stroke-width="1.8"/></svg>
          dale@rankharbor.com.au
        </li>
        <li class="contact-item">
          <svg class="contact-icon" viewBox="0 0 24 24" aria-hidden="true"><g fill="none" stroke="var(--blue)" stroke-width="1.6"><circle cx="12" cy="12" r="9.5"/><ellipse cx="12" cy="12" rx="4.2" ry="9.5"/><path d="M2.5 12h19M4 7h16M4 17h16"/></g></svg>
          www.rankharbor.com.au
        </li>
      </ul>
    </section>

    <div class="ribbon-band" role="img" aria-label="Blue panel where a yellow folded ribbon zigzags upward across the lower card"></div>
  </main>
</body>
</html>
```